MODELS AGENCY NEW YEAR 2026 CARD

A 10 cm x 21 cm horizontal New Year card for clients of our 2 models agencies, Pommelin (kids) and Velvaride (actors and adults) (logo in the jobs).

Side A of the card: creative mission:
-text: 2026
-text: Peace and Love
-Studio or movie set atmosphere
-tone of voice: optimistic, positive, colorful

Side B:
(name of 4 people of the agency:)
Odette, Anne-Sophie, Hortense & Luc-Antoine,
(2 logos)
Pommelin & VelvaRide
(Adres)
Rue des Tilleuls 74 b3 - 1200 Bruxelles - Belgique

Target Market(s)

Movie directors, photographers

Industry/Entity Type

Fashion, advertising & Movies

Requirements
Must have
• SEE TEXT IN BRIEFING

```html
<!DOCTYPE html>
<html lang="en">
<head>
<meta charset="utf-8">
<title>Pommelin &amp; Velvaride — New Year 2026 Card</title>
<link rel="stylesheet" href="https://fonts.googleapis.com/css2?family=Poppins:wght@500;600;700;800&family=Great+Vibes&display=swap">
<style>
  :root {
    --backdrop: #8f9092;
    --card-white: #ffffff;
    --night-purple: #2a1850;
    --stage-violet: #5b2f95;
    --stage-red: #b2224a;
    --stage-amber: #d9822b;
    --orange: #f05a22;
    --cyan: #13aee8;
    --purple: #3d2470;
    --teal: #1a8bb0;
    --ink: #111111;
    --props-grey: #c9cacd;
  }
  * { margin: 0; padding: 0; box-sizing: border-box; }
  html, body {
    width: 1200px; height: 1194px; overflow: hidden;
    background: var(--backdrop);
  }
  .sheet { position: relative; width: 1200px; height: 1194px; }

  /* Side A */
  .side-a {
    position: absolute; left: 74px; top: 85px; width: 1038px; height: 493px;
    overflow: hidden;
  }
  .side-a .stage-scene {
    position: absolute; inset: 0;
    background:
      radial-gradient(ellipse 30% 45% at 50% 20%, rgba(70,140,170,.5), transparent 70%),
      radial-gradient(ellipse 16% 40% at 28% 45%, rgba(217,130,43,.55), transparent 70%),
      radial-gradient(ellipse 16% 40% at 74% 45%, rgba(217,130,43,.55), transparent 70%),
      radial-gradient(ellipse 60% 35% at 45% 100%, rgba(178,34,74,.85), transparent 75%),
      linear-gradient(90deg, var(--stage-violet) 0%, var(--night-purple) 25%, #1a1430 50%, var(--night-purple) 75%, var(--stage-violet) 100%);
  }
  .side-a .greeting {
    position: absolute; left: 0; right: 0; top: 92px;
    text-align: center; color: var(--card-white);
    font-family: "Great Vibes", cursive; font-size: 74px; line-height: 1;
    transform: translateX(10px);
  }
  .side-a .year {
    position: absolute; left: 0; right: 0; top: 157px;
    text-align: center; color: var(--card-white);
    font-family: "Poppins", sans-serif; font-weight: 700;
    font-size: 212px; line-height: 1; letter-spacing: -4px;
    transform: translateX(8px);
    text-shadow: 0 4px 14px rgba(0,0,0,.35);
  }

  /* Side B */
  .side-b {
    position: absolute; left: 74px; top: 634px; width: 1035px; height: 491px;
    overflow: hidden;
    background: linear-gradient(180deg, #ffffff 0%, #f4f4f5 60%, #e9e9ea 100%);
  }
  .side-b .props-photo {
    position: absolute; right: 0; top: 0; width: 600px; height: 491px;
    background:
      radial-gradient(ellipse 70% 75% at 80% 55%, rgba(90,92,96,.55), transparent 75%),
      linear-gradient(90deg, rgba(255,255,255,0) 0%, rgba(220,221,224,.7) 40%, var(--props-grey) 100%);
  }
  .agency-marks {
    position: absolute; left: 50px; top: 72px; display: flex; gap: 32px;
  }
  .agency-mark {
    display: flex; align-items: center; gap: 8px;
    font-family: "Poppins", sans-serif; font-weight: 700; font-size: 26px;
    color: var(--purple);
  }
  .agency-mark .dot { width: 14px; height: 14px; border-radius: 50%; }
  .agency-mark.velvaride .dot { background: var(--orange); }
  .agency-mark.pommelin .dot { background: var(--cyan); }

  .team {
    position: absolute; left: 50px; top: 168px; list-style: none;
    font-family: "Poppins", sans-serif; font-weight: 600;
    font-size: 48px; line-height: 51px; letter-spacing: -1px;
  }
  .team .orange { color: var(--orange); }
  .team .cyan { color: var(--cyan); }
  .team .purple { color: var(--purple); }
  .team .teal { color: var(--teal); }

  .address-band {
    position: absolute; left: 24px; top: 406px; width: 692px; height: 48px;
  }
  .address-band svg { position: absolute; inset: 0; }
  .address-band p {
    position: relative; line-height: 48px; text-align: center;
    font-family: "Poppins", sans-serif; font-weight: 600; font-size: 20px;
    color: var(--card-white); letter-spacing: -.3px;
  }
</style>
</head>
<body>
<main class="sheet">
  <section class="side-a">
    <div class="stage-scene" role="img" aria-label="Movie studio stage with curtains, warm lights, film reels and a director's chair"></div>
    <p class="greeting">Peace and Love</p>
    <p class="year">2026</p>
  </section>

  <section class="side-b">
    <div class="props-photo" role="img" aria-label="Clapperboard, 3D glasses and film reels on a white surface"></div>

    <div class="agency-marks">
      <div class="agency-mark velvaride"><span class="dot"></span>Velvaride</div>
      <div class="agency-mark pommelin"><span class="dot"></span>Pommelin</div>
    </div>

    <ul class="team">
      <li class="orange">Odette</li>
      <li class="cyan">Anne-Sophie</li>
      <li class="purple">Hortense</li>
      <li class="teal">Luc-Antoine</li>
    </ul>

    <div class="address-band">
      <svg viewBox="0 0 692 48" preserveAspectRatio="none" aria-hidden="true">
        <path d="M0 22 L40 6 L640 3 L660 10 L692 14 L670 24 L688 34 L650 40 L560 46 L70 45 L20 40 L36 32 Z" fill="var(--ink)"/>
      </svg>
      <p>Rue des Tilleuls 74 b3 - 1200 Bruxelles - Belgique</p>
    </div>
  </section>
</main>
</body>
</html>
```